Kai & Palz

I am looking for help designing a concert benefit flyer. I recently designed a ticket for the event. Attached is the font and the back.
The event is being thrown for Kai Bennett Lo'o Lo'o Haver – He is IMAGE 5112 / 5113/5110 ( I have uploaded 3 options – just use the best that you think would work)
We have 7 different artist’s who will be showcased in the event that we would like to incorporate in the flyer
Image 5107 is the main Artist
“ Buro and the list below is his Palz”
Image 5101 is “Pualu”
Image 5102 is Tobin Garcela
Image 5103 is Ikaika Lopes
Image 5104 is Marisa Dutra
Image 5106 is Ilima Segundo
Image 5109 is “Manuheali”
I have uploaded an old flyer we created for a smaller event and was wondering if you could help us design this one ?
Please let me know if you can help and I will go into further details?
Corinne Talua
HALEWAI MANAGEMENT

```html
<!DOCTYPE html>
<html lang="en">
<head>
<meta charset="utf-8">
<title>Kai &amp; Palz – A Benefit Concert</title>
<link href="https://fonts.googleapis.com/css2?family=Permanent+Marker&family=Playfair+Display:ital,wght@0,800;1,700&family=Yellowtail&family=Montserrat:wght@400;500;600;700&family=Roboto+Slab:wght@700;800&display=swap" rel="stylesheet">
<style>
  :root{
    --page:#e9e9e9;
    --ink:#0b0806;
    --gold:#f2d21f;
    --gold-deep:#c9a40f;
    --amber:#f29a12;
    --red:#c8141b;
    --red-deep:#7e0a0e;
    --white:#ffffff;
    --silver:#bfc3c7;
  }
  *{margin:0;padding:0;box-sizing:border-box}
  html,body{width:1200px;height:2488px;overflow:hidden;background:var(--page)}
  .flyer{
    position:absolute;left:50px;top:465px;width:1100px;height:1557px;
    background:
      radial-gradient(ellipse 420px 300px at 50% 420px, rgba(242,154,18,.55), transparent 70%),
      radial-gradient(circle 260px at 12% 78%, rgba(200,120,20,.18), transparent 70%),
      radial-gradient(circle 300px at 90% 60%, rgba(200,120,20,.14), transparent 70%),
      var(--ink);
    box-shadow:0 20px 40px rgba(0,0,0,.35);
    color:var(--white);
    font-family:"Montserrat",sans-serif;
  }
  .frame{position:absolute;inset:0}
  .title{
    position:absolute;top:85px;width:100%;text-align:center;
    font-family:"Permanent Marker",cursive;font-size:124px;line-height:1;color:#f1f1f1;
  }
  .hero{
    position:absolute;left:110px;top:230px;width:880px;height:380px;border-radius:50%;
    background:radial-gradient(ellipse at 50% 50%, #ffb21e 0%, #d77a08 35%, rgba(120,60,0,.5) 60%, transparent 75%);
  }
  .portrait{
    position:absolute;left:420px;top:250px;width:260px;height:340px;border-radius:130px 130px 20px 20px;
    background:linear-gradient(#7a5a3a,#caa183 45%,#d9d4cc);
  }
  .headline{
    position:absolute;top:525px;width:100%;text-align:center;
    font-family:"Playfair Display",serif;font-weight:800;font-size:148px;line-height:1;
    background:linear-gradient(180deg,#ffffff 20%,var(--silver) 55%,#6d7075 80%,#e6e6e6);
    -webkit-background-clip:text;background-clip:text;color:transparent;
  }
  .headline-script{
    position:absolute;top:665px;left:330px;
    font-family:"Yellowtail",cursive;font-size:118px;line-height:1;color:var(--gold);
  }
  .honoree{
    position:absolute;top:800px;width:100%;text-align:center;
    font-weight:600;font-size:26px;letter-spacing:7px;
  }
  .details{
    position:absolute;top:850px;left:190px;width:720px;display:flex;
  }
  .detail{flex:1;text-align:center;padding:6px 0}
  .detail + .detail{border-left:3px solid var(--red)}
  .detail-label{color:var(--gold);font-weight:600;font-size:21px;letter-spacing:1px}
  .detail-value{font-family:"Playfair Display",serif;font-style:italic;font-weight:700;font-size:34px;line-height:1.05}
  .detail-value.venue{font-size:24px;font-weight:400;line-height:1.2}
  .to{display:inline-block;width:28px;height:28px;border-radius:50%;background:var(--red);font-size:18px;line-height:26px;vertical-align:middle}
  .ticket-row{position:absolute;top:965px;left:170px;display:flex;align-items:center}
  .ticket-art{width:182px;height:68px;transform:rotate(6deg);background:linear-gradient(90deg,#111 60%,var(--gold) 60%,#e9c62a);border:1px solid #555}
  .ticket-banner{
    margin-left:-6px;width:560px;height:50px;border-radius:0 10px 10px 0;
    background:linear-gradient(var(--red),var(--red-deep));
    font-family:"Roboto Slab",serif;font-weight:800;font-size:32px;letter-spacing:5px;line-height:50px;text-align:center;
  }
  .music{position:absolute;top:1037px;width:100%;text-align:center;font-family:"Roboto Slab",serif;font-weight:700;font-size:37px;color:var(--gold)}
  .entertainment{position:absolute;top:1090px;width:100%;text-align:center;font-size:25px}
  .entertainment strong{color:var(--gold);font-weight:700}
  .rule{position:absolute;top:1137px;left:175px;width:750px;height:1px;background:linear-gradient(90deg,transparent,#777,transparent)}
  .featuring{position:absolute;top:1148px;width:100%;text-align:center;font-family:"Roboto Slab",serif;font-weight:800;font-size:28px;letter-spacing:8px;color:var(--gold)}
  .lineup{position:absolute;top:1192px;left:136px;width:830px;display:flex;border:3px solid var(--white);gap:3px;background:var(--white)}
  .artist-photo{flex:1;height:134px;background:linear-gradient(160deg,#6a4a35,#2b2019)}
  .artist-photo.alt{background:linear-gradient(160deg,#b36a48,#3b2418)}
  .artist-mark{flex:1;height:134px;background:#1a1a1a;display:flex;align-items:center;justify-content:center;font-weight:600;font-size:13px}
  .names{position:absolute;top:1342px;left:136px;width:830px;display:flex}
  .name{flex:1;text-align:center;font-size:17px;line-height:1.1}
  .name b{font-weight:700;display:block}
  .credits{position:absolute;top:1402px;width:100%;text-align:center;font-size:23px;line-height:1.5}
  .credits span{font-family:"Roboto Slab",serif;font-weight:800;color:var(--gold);font-size:25px}
</style>
</head>
<body>
<main class="flyer">
  <svg class="frame" width="1100" height="1557" viewBox="0 0 1100 1557" aria-hidden="true">
    <polygon points="118,50 1047,50 1047,1443 985,1505 53,1505 53,115" fill="none" stroke="#f2d21f" stroke-width="4"/>
    <polygon points="124,62 1035,62 1035,1438 980,1493 65,1493 65,120" fill="none" stroke="#c9a40f" stroke-width="1.5"/>
  </svg>

  <h1 class="title">Kai &amp; Palz</h1>

  <div class="hero" role="img" aria-label="Golden glowing sound-wave equalizer with dancing silhouettes"></div>
  <div class="portrait" role="img" aria-label="Portrait of Kai Bennett Lo'o Lo'o Haver in a flat cap"></div>

  <h2 class="headline">A Benefit</h2>
  <p class="headline-script">Concert</p>

  <p class="honoree">FOR KAI BENNETT LO'O LO'O HAVER</p>

  <section class="details">
    <div class="detail"><div class="detail-label">DATE</div><div class="detail-value">March 9<sup>th</sup><br><span style="font-weight:400">2024</span></div></div>
    <div class="detail"><div class="detail-label">TIME</div><div class="detail-value">4pm <span class="to">to</span> 8pm</div></div>
    <div class="detail"><div class="detail-label">VENUE</div><div class="detail-value venue">Palmcrest Lu'au<br>Pavillion</div></div>
  </section>

  <div class="ticket-row">
    <div class="ticket-art" role="img" aria-label="Event ticket for Buro &amp; Palz"></div>
    <div class="ticket-banner">TICKETED ENTRY ONLY</div>
  </div>

  <p class="music">Live Hawaiian Music</p>
  <p class="entertainment">Entertainment by the <strong>"Mimosa Mamas"</strong> and <strong>Live Raffle</strong> Giveaway</p>
  <div class="rule"></div>

  <h3 class="featuring">FEATURING MUSIC BY</h3>
  <div class="lineup">
    <div class="artist-photo" role="img" aria-label="Tobin Garcela with guitar"></div>
    <div class="artist-photo alt" role="img" aria-label="Marisa Dutra wearing a flower crown"></div>
    <div class="artist-photo alt" role="img" aria-label="Pualu duo with ukulele"></div>
    <div class="artist-photo" role="img" aria-label="Keoni Alapai with ukulele"></div>
    <div class="artist-photo" role="img" aria-label="Ilima Segundo with a flower in her hair"></div>
    <div class="artist-photo alt" role="img" aria-label="Ikaika Lopes in a cowboy hat"></div>
    <div class="artist-mark">MANUHEALI</div>
  </div>
  <div class="names">
    <p class="name"><b>TOBIN</b>GARCELA</p>
    <p class="name"><b>MARISA</b>DUTRA</p>
    <p class="name"><b>PUALU</b></p>
    <p class="name"><b>KEONI</b>ALAPAI</p>
    <p class="name"><b>ILIMA</b>SEGUNDO</p>
    <p class="name"><b>IKAIKA</b>LOPES</p>
    <p class="name"><b>MANUHEALI</b>PRODUCTIONS</p>
  </div>

  <p class="credits"><span>EVENT HOSTED BY:</span> Halewai Management Group<br><span>CASH BAR:</span> Cash Event</p>
</main>
</body>
</html>
```